Design the Keystone HR business card for my new business

I've just had a logo designed (attached) for my new business doing HR consulting. I'm a one person operation at this stage, my aim is to provide support and help to small to medium sized businesses with their people objectives or issues.

I'm not really into anything overly flashy, I'm not a PR or marketing agency. I'd like my card to look modern, professional and not gimmicky.

I'm thinking black front (to go with logo), double sided with details on the back, maybe in a different colour?

Logo attached in several different formats.

Front of the card to have logo and added text: People and Development Solutions

Back of the card to also feature logo in some way and say:
Megan Tulloch
PO Box (TBA)
Marrowvale QLD 4391
0438 512 976
megan@keystonehr.com.au
www.keystonehr.com.au

Target Market(s)

Small to medium businesses / business owners.

Industry/Entity Type

Marketing

Requirements
Must have
• Double sided business card.
Should not have
• Anything overly gimmicky.

```html
<!DOCTYPE html>
<html lang="en">
<head>
<meta charset="utf-8">
<title>Keystone HR Consulting – Business Card</title>
<link href="https://fonts.googleapis.com/css2?family=Questrial&display=swap" rel="stylesheet">
<style>
  :root {
    --backdrop: #bde0cd;
    --card-dark: #000000;
    --card-light: #ffffff;
    --ink-light: #ffffff;
    --ink-dark: #2a2a2a;
    --accent: #5b2fd6;
    --accent-soft: #8f6cf0;
    --rule: #555555;
  }
  * { margin: 0; padding: 0; box-sizing: border-box; }
  html, body { width: 1200px; height: 900px; overflow: hidden; }
  body {
    background: var(--backdrop);
    font-family: "Questrial", "Century Gothic", sans-serif;
    position: relative;
  }
  .card {
    position: absolute;
    width: 576px;
    height: 332px;
    overflow: hidden;
  }

  /* Front */
  .card-front {
    left: 88px; top: 100px;
    background: var(--card-dark);
    color: var(--ink-light);
  }
  .brand-dot {
    position: absolute;
    left: 60px; top: 58px;
    width: 120px; height: 120px;
    border-radius: 50%;
    background: var(--accent);
  }
  .brand-name {
    position: absolute;
    right: 60px; top: 40px;
    text-align: right;
    font-weight: 400;
    color: var(--ink-light);
  }
  .brand-name .primary { display: block; font-size: 76px; line-height: 1; letter-spacing: -1px; }
  .brand-name .secondary { display: block; font-size: 30px; line-height: 1.3; margin-top: 4px; }
  .tagline {
    position: absolute;
    left: 44px; top: 254px;
    font-size: 24px;
    letter-spacing: 0.5px;
  }

  /* Back */
  .card-back {
    left: 508px; top: 476px;
    background: var(--card-light);
    color: var(--ink-dark);
    box-shadow: 0 0 0 1px #e4e4e4;
  }
  .back-dot {
    position: absolute;
    right: -40px; top: -40px;
    width: 220px; height: 220px;
    border-radius: 50%;
    background: var(--accent);
  }
  .details {
    position: absolute;
    left: 64px; top: 72px;
    list-style: none;
  }
  .details li {
    display: flex;
    align-items: center;
    height: 58px;
    font-size: 23px;
  }
  .details li::before {
    content: "";
    width: 24px; height: 24px;
    border-radius: 50%;
    background: var(--accent-soft);
    margin-right: 24px;
  }
  .contact-rule {
    position: absolute;
    left: 48px; right: 28px; top: 262px;
    border-top: 1px solid var(--rule);
  }
  .contact-row {
    position: absolute;
    left: 48px; right: 28px; top: 272px;
    display: flex;
    justify-content: space-between;
    font-size: 15px;
  }
</style>
</head>
<body>
  <section class="card card-front" aria-label="Card front">
    <div class="brand-dot" aria-hidden="true"></div>
    <h1 class="brand-name">
      <span class="primary">Keystone</span>
      <span class="secondary">HR Consulting</span>
    </h1>
    <p class="tagline">People and Development Solutions</p>
  </section>

  <section class="card card-back" aria-label="Card back">
    <div class="back-dot" aria-hidden="true"></div>
    <ul class="details">
      <li>Megan Tulloch</li>
      <li>PO Box (TBA)</li>
      <li>Marrowvale QLD 4391</li>
    </ul>
    <div class="contact-rule"></div>
    <p class="contact-row">
      <span>0438 512 976</span>
      <span>megan@keystonehr.com.au</span>
      <span>www.keystonehr.com.au</span>
    </p>
  </section>
</body>
</html>
```